Real Estate "For Sale" Sign for construction company

We need a sign that we can use to hang on a post and place on the road when we sell a property. The sign will be simple and will need to mainly feature our logo (files attached), as well as the words "For Sale", and then our phone number "(555) 617 3489". The sign will hang on a post that'll look something like the attached picture.

Target Market(s)

Home buyers

Industry/Entity Type

Real Estate

Font styles to use
Serif
Sans Serif

Colors
0054AA
0677BA
7BADD7
CADEEF
E8F1F8
0094D4
00A9DD
6FCCEA
C7EBF8
E9F6FB

Requirements
Must have
• For Sale & our phone number

```html
<!DOCTYPE html>
<html lang="en">
<head>
<meta charset="utf-8">
<title>For Sale – Ridgeline Crest Homes</title>
<link rel="stylesheet" href="https://fonts.googleapis.com/css2?family=Jost:ital,wght@1,800&family=Lexend:wght@400&family=Unbounded:wght@800&display=swap">
<style>
  :root {
    --brand-blue: #0050a4;
    --sky: #cae9f9;
    --logo-blue: #1a7bc1;
    --white: #ffffff;
  }
  html, body {
    margin: 0;
    padding: 0;
    overflow: hidden;
    background: var(--sky);
  }
  .sign {
    position: relative;
    width: 776px;
    height: 1200px;
    background: var(--sky);
    overflow: hidden;
  }
  .sign__header {
    position: absolute;
    left: 0; top: 0;
    width: 776px; height: 207px;
    background: var(--brand-blue);
  }
  .sign__headline {
    position: absolute;
    left: 0; top: 0;
    width: 776px; height: 207px;
  }
  .sign__headline text {
    font-family: "Jost", "Futura", sans-serif;
    font-style: italic;
    font-weight: 800;
    fill: var(--white);
  }
  .brand {
    position: absolute;
    left: 0; top: 320px;
    width: 776px;
    text-align: center;
    color: var(--logo-blue);
    font-family: "Lexend", sans-serif;
    font-weight: 400;
  }
  .brand__dot {
    width: 300px;
    height: 300px;
    margin: 0 auto 66px;
    border-radius: 50%;
    background: var(--logo-blue);
  }
  .brand__name {
    margin: 0;
    font-size: 54px;
    line-height: 1;
    letter-spacing: 0.5px;
  }
  .brand__tag {
    margin: 22px 0 0 18px;
    font-size: 20px;
    letter-spacing: 28px;
  }
  .sign__footer {
    position: absolute;
    left: 0; top: 1052px;
    width: 776px; height: 148px;
    background: var(--brand-blue);
  }
  .sign__phone text {
    font-family: "Unbounded", sans-serif;
    font-weight: 800;
    fill: var(--white);
  }
</style>
</head>
<body>
  <main class="sign">
    <header class="sign__header">
      <svg class="sign__headline" viewBox="0 0 776 207" width="776" height="207">
        <text x="55" y="156" font-size="150" textLength="666" lengthAdjust="spacingAndGlyphs">FOR SALE</text>
      </svg>
    </header>

    <section class="brand">
      <div class="brand__dot"></div>
      <p class="brand__name">Ridgeline Crest</p>
      <p class="brand__tag">HOMES</p>
    </section>

    <footer class="sign__footer">
      <svg class="sign__phone" viewBox="0 0 776 148" width="776" height="148">
        <text x="45" y="98" font-size="66" textLength="686" lengthAdjust="spacingAndGlyphs">(555) 617-3489</text>
      </svg>
    </footer>
  </main>
</body>
</html>
```